Packaging Design New Cosmetics Range

Small Establish online Beauty company is expanding it's product range into Serums, Sprays and Creams . We are looking for a new fresh packaging design for this launch.
We only use products that are Organic , Not Tested on Animals and Natural products
We would be interested in viewing a White Design , Black design and a designer choice of colors .
First Products are
Rose Water in 100ml glass bottle with box
and a set of 3 Face Serums Vit C , Retinol and Hyaluronic in 30ml Glass bottle = Box
Scrubs and creams will launch later in Q1 2020 however would like a similar feel across all products
Target Market(s)
SEA / US Markets
Industry/Entity Type
Cosmetics
Colors
Designer to choose colors to be used in the design.
Requirements
Must have
- Space Allocated for Product Use and Bar Codes on Box
Nice to have
- Organic , Not tested on animal Logo's

```html
<!DOCTYPE html>
<html lang="en">
<head>
<meta charset="utf-8">
<title>Rose Water Folding Carton – Black</title>
<link rel="stylesheet" href="https://fonts.googleapis.com/css2?family=Antonio:wght@200;300;400&family=Source+Sans+3:wght@400&display=swap">
<style>
  :root {
    --key-line: #00f0ff;
    --brand-green: #1ef06a;
    --rose-red: #e8140f;
    --carton-black: #000000;
    --text-white: #ffffff;
    --paper: #ffffff;
    --label-ink: #111111;
  }
  html, body {
    margin: 0;
    padding: 0;
    width: 862px;
    height: 1200px;
    overflow: hidden;
    background: var(--paper);
  }
  .artboard { display: block; width: 862px; height: 1200px; }

  .sheet-title, .sheet-subtitle, .dimension-label {
    fill: var(--key-line);
    font-family: "Source Sans 3", sans-serif;
  }
  .sheet-title { font-size: 50px; }
  .sheet-subtitle { font-size: 50px; }
  .dimension-label { font-size: 50px; }
  .dimension-label.large { font-size: 72px; }

  .dimension-line { stroke: var(--key-line); stroke-width: 1.5; fill: none; }
  .key-line { stroke: var(--key-line); stroke-width: 1.5; fill: none; }
  .glue-flap { stroke: var(--key-line); stroke-width: 1.5; fill: var(--paper); }
  .carton-board { fill: var(--carton-black); }

  .panel-heading {
    fill: var(--brand-green);
    font-family: "Antonio", sans-serif;
    font-weight: 300;
    font-size: 27px;
    letter-spacing: 1px;
  }
  .brand-name {
    fill: var(--brand-green);
    font-family: "Antonio", sans-serif;
    font-weight: 300;
    font-size: 46px;
  }
  .product-name {
    fill: var(--text-white);
    font-family: "Antonio", sans-serif;
    font-weight: 200;
    font-size: 46px;
    letter-spacing: 3px;
  }
  .product-volume {
    fill: var(--text-white);
    font-family: "Antonio", sans-serif;
    font-weight: 200;
    font-size: 36px;
  }
  .info-box { fill: var(--paper); }
  .info-box-label {
    fill: #a8f4f8;
    font-family: "Antonio", sans-serif;
    font-weight: 300;
    font-size: 22px;
    letter-spacing: 3px;
  }
  .rose-artwork { fill: var(--rose-red); }
  .organic-badge { fill: var(--brand-green); }

  .colour-guide-title, .swatch-label {
    fill: var(--label-ink);
    font-family: "Antonio", sans-serif;
    font-weight: 300;
    font-size: 24px;
  }
  .swatch-green { fill: var(--brand-green); }
  .swatch-red { fill: var(--rose-red); }
  .swatch-black { fill: var(--carton-black); }
  .swatch-key { fill: var(--key-line); }
</style>
</head>
<body>
<svg class="artboard" viewBox="0 0 1654 2339" preserveAspectRatio="xMidYMid meet" xmlns="http://www.w3.org/2000/svg">

  <!-- Sheet header -->
  <g class="sheet-header">
    <text class="sheet-title" x="276" y="110">ROSE WATER FOLDING CARTON DESIGN- BLACK</text>
    <text class="sheet-subtitle" x="276" y="200">All dimensions in mm</text>
  </g>

  <!-- Overall width dimension -->
  <g class="dimension-width">
    <text class="dimension-label large" x="826" y="290" text-anchor="middle">155</text>
    <line class="dimension-line" x1="276" y1="340" x2="1374" y2="340"/>
    <line class="dimension-line" x1="276" y1="288" x2="276" y2="392"/>
    <line class="dimension-line" x1="1374" y1="288" x2="1374" y2="392"/>
  </g>

  <!-- Overall height dimension -->
  <g class="dimension-height">
    <line class="dimension-line" x1="170" y1="446" x2="170" y2="1933"/>
    <line class="dimension-line" x1="117" y1="446" x2="222" y2="446"/>
    <line class="dimension-line" x1="117" y1="1933" x2="222" y2="1933"/>
    <text class="dimension-label large" x="0" y="0" text-anchor="middle" transform="translate(96 1040) rotate(-90)">210</text>
  </g>

  <!-- Section heights -->
  <g class="dimension-sections">
    <line class="dimension-line" x1="1480" y1="446" x2="1480" y2="1933"/>
    <line class="dimension-line" x1="1427" y1="446" x2="1533" y2="446"/>
    <line class="dimension-line" x1="1427" y1="534" x2="1533" y2="534"/>
    <line class="dimension-line" x1="1427" y1="601" x2="1533" y2="601"/>
    <line class="dimension-line" x1="1427" y1="778" x2="1533" y2="778"/>
    <line class="dimension-line" x1="1427" y1="1593" x2="1533" y2="1593"/>
    <line class="dimension-line" x1="1427" y1="1770" x2="1533" y2="1770"/>
    <line class="dimension-line" x1="1427" y1="1838" x2="1533" y2="1838"/>
    <line class="dimension-line" x1="1427" y1="1933" x2="1533" y2="1933"/>
    <text class="dimension-label" x="1515" y="515">12.5</text>
    <text class="dimension-label" x="1515" y="583">9.5</text>
    <text class="dimension-label" x="1515" y="718">25</text>
    <text class="dimension-label" x="1515" y="1100">115</text>
    <text class="dimension-label" x="1515" y="1708">25</text>
    <text class="dimension-label" x="1515" y="1820">9.5</text>
    <text class="dimension-label" x="1515" y="1908">12.5</text>
  </g>

  <!-- Panel widths -->
  <g class="dimension-panels">
    <line class="dimension-line" x1="276" y1="2040" x2="1374" y2="2040"/>
    <line class="dimension-line" x1="276" y1="1988" x2="276" y2="2092"/>
    <line class="dimension-line" x1="382" y1="1988" x2="382" y2="2092"/>
    <line class="dimension-line" x1="630" y1="1988" x2="630" y2="2092"/>
    <line class="dimension-line" x1="878" y1="1988" x2="878" y2="2092"/>
    <line class="dimension-line" x1="1126" y1="1988" x2="1126" y2="2092"/>
    <line class="dimension-line" x1="1374" y1="1988" x2="1374" y2="2092"/>
    <text class="dimension-label" x="326" y="2112" text-anchor="middle">15</text>
    <text class="dimension-label" x="482" y="2112" text-anchor="middle">35</text>
    <text class="dimension-label" x="752" y="2112" text-anchor="middle">35</text>
    <text class="dimension-label" x="1022" y="2112" text-anchor="middle">35</text>
    <text class="dimension-label" x="1292" y="2112" text-anchor="middle">35</text>
  </g>

  <!-- Carton dieline -->
  <g class="carton">
    <polygon class="glue-flap" points="382,783 276,817 276,1562 382,1597"/>

    <!-- Printed board -->
    <path class="carton-board" d="M360 783 L360 480 Q360 423 410 423 L600 423 Q652 423 652 490 L652 530 L648 583 L865 583 L900 745 L878 783 Z"/>
    <path class="carton-board" d="M1126 783 L1104 745 L1140 583 L1382 583 L1382 745 L1396 783 Z"/>
    <rect class="carton-board" x="360" y="783" width="1036" height="814"/>
    <path class="carton-board" d="M630 1597 L608 1633 L643 1797 L856 1797 L856 1920 Q856 1955 895 1955 L1110 1955 Q1148 1955 1148 1920 L1148 1605 L1160 1633 L1160 1797 L1362 1797 L1396 1633 L1396 1597 Z"/>

    <!-- Fold and cut key lines -->
    <path class="key-line" d="M382 783 L382 490 Q382 446 426 446 L586 446 Q630 446 630 490 L630 783"/>
    <line class="key-line" x1="382" y1="534" x2="630" y2="534"/>
    <path class="key-line" d="M630 783 L665 748 L665 606 L843 606 L878 748 L878 783"/>
    <path class="key-line" d="M1126 783 L1126 748 L1160 606 L1338 606 L1338 748 L1374 783"/>
    <rect class="key-line" x="382" y="783" width="992" height="814"/>
    <line class="key-line" x1="630" y1="783" x2="630" y2="1597"/>
    <line class="key-line" x1="878" y1="783" x2="878" y2="1597"/>
    <line class="key-line" x1="1126" y1="783" x2="1126" y2="1597"/>
    <path class="key-line" d="M630 1597 L665 1774 L843 1774 L843 1633 L878 1597"/>
    <path class="key-line" d="M878 1597 L878 1890 Q878 1933 921 1933 L1083 1933 Q1126 1933 1126 1890 L1126 1597"/>
    <line class="key-line" x1="878" y1="1843" x2="1126" y2="1843"/>
    <path class="key-line" d="M1126 1597 L1160 1633 L1160 1774 L1338 1774 L1374 1633 L1374 1597"/>

    <!-- Front panel -->
    <g class="panel-front">
      <text class="brand-name" x="506" y="972" text-anchor="middle">lunavel</text>
      <text class="product-name" x="502" y="1110" text-anchor="middle">ROSE WATER</text>
      <ellipse class="rose-artwork" cx="506" cy="1272" rx="86" ry="68" role="img" aria-label="Photograph of a red rose bloom"/>
      <text class="product-volume" x="503" y="1548" text-anchor="middle">100 ml</text>
    </g>

    <!-- Directions panel -->
    <g class="panel-directions">
      <text class="panel-heading" x="748" y="851" text-anchor="middle">DIRECTIONS FOR USE</text>
      <rect class="info-box" x="683" y="1020" width="142" height="106"/>
      <text class="info-box-label" x="750" y="1064" text-anchor="middle">CODING</text>
      <text class="info-box-label" x="752" y="1094" text-anchor="middle">SAPCE</text>
      <rect class="info-box" x="683" y="1189" width="142" height="268"/>
      <text class="info-box-label" x="0" y="0" text-anchor="middle" transform="translate(759 1318) rotate(-90)">BARCODE</text>
      <text class="panel-heading" x="762" y="1526" text-anchor="middle">STORAGE INSTRUCTIONS</text>
    </g>

    <!-- Back panel -->
    <g class="panel-back">
      <text class="brand-name" x="1002" y="972" text-anchor="middle">lunavel</text>
      <text class="product-name" x="998" y="1110" text-anchor="middle">ROSE WATER</text>
      <ellipse class="rose-artwork" cx="1002" cy="1272" rx="86" ry="68" role="img" aria-label="Photograph of a red rose bloom"/>
      <text class="product-volume" x="999" y="1548" text-anchor="middle">100 ml</text>
    </g>

    <!-- Ingredients panel -->
    <g class="panel-ingredients">
      <text class="panel-heading" x="1248" y="873" text-anchor="middle">INGREDIENTS</text>
      <circle class="organic-badge" cx="1250" cy="1218" r="53"/>
      <text class="panel-heading" x="1248" y="1368" text-anchor="middle">PRODUCED &amp;</text>
      <text class="panel-heading" x="1248" y="1401" text-anchor="middle">PACKED BY</text>
    </g>
  </g>

  <!-- Colour guide -->
  <g class="colour-guide">
    <text class="colour-guide-title" x="278" y="2157">COLOUR GUIDE</text>
    <rect class="swatch-green" x="276" y="2188" width="35" height="35"/>
    <text class="swatch-label" x="316" y="2222">PANTONE 3268 C</text>
    <rect class="swatch-red" x="501" y="2188" width="35" height="35"/>
    <text class="swatch-label" x="546" y="2222">PANTONE 485 C</text>
    <rect class="swatch-black" x="725" y="2188" width="35" height="35"/>
    <text class="swatch-label" x="769" y="2222">BLACK</text>
    <rect class="swatch-key" x="1108" y="2188" width="35" height="35"/>
    <text class="swatch-label" x="1160" y="2222">KEY LINES</text>
  </g>
</svg>
</body>
</html>
```